Tarbery's - Irish Shortbread

Tarbery’s Irish Shortbread
We are looking for a Stand-Up Pouch design – (no window no zip) that will have different flavoured all-butter shortbread in the collection. We love vintage and kitsch as a company but do not have to head in that direction. We are font lovers and would happily have a Font Driven Design for packaging. For this project we were thinking about water colours to define the flavours or Graffiti Package Design. We have 6 flavours, they are:
Irish Shortbread - Ginger Shortbread - Espresso Shortbread - Parmesan and Poppy Seed Shortbread - Strawberry Shortbread - Butterscotch Shortbread.
The size of the pouch is 12cm x 17 cm. There needs to be a hanging hole at the top. We have uploaded a couple of images. What we like is the intensity of colour, clarity of flavour and words. This needs to feel familiar yet fresh on the shelf and not merge with other packaging at the supermarket.
We are also fans of 80s Graffiti designs for packaging – see a few attached images.
I have also attached the brand

```html
<!DOCTYPE html>
<html lang="en">
<head>
<meta charset="utf-8">
<title>Tarbery’s Irish Shortbread – Butterscotch Pouch</title>
<link rel="stylesheet" href="https://fonts.googleapis.com/css2?family=Bebas+Neue&family=Poppins:wght@500&display=swap">
<style>
  :root {
    --backdrop: #e6e6e6;
    --pouch-white: #f6f6f4;
    --wash-deep: #f0cc4a;
    --wash-mid: #f4dc6c;
    --wash-light: #f8ec9e;
    --gold: #e1b63a;
    --ink: #3a3a3a;
  }
  * { margin: 0; padding: 0; box-sizing: border-box; }
  html, body {
    width: 1200px; height: 1014px; overflow: hidden;
    background: var(--backdrop);
  }
  .pouch {
    position: absolute; left: 335px; top: 57px;
    width: 530px; height: 900px;
    background: var(--pouch-white);
    border-radius: 24px 24px 10px 10px;
    overflow: hidden;
    color: var(--ink);
    font-family: "Bebas Neue", "Arial Narrow", sans-serif;
    text-align: center;
  }
  .pouch__wash {
    position: absolute; inset: 0;
    background:
      radial-gradient(ellipse 42% 20% at 32% 8%, var(--wash-deep), transparent 70%),
      radial-gradient(ellipse 30% 16% at 82% 12%, var(--wash-light), transparent 70%),
      radial-gradient(ellipse 22% 30% at 4% 34%, var(--wash-mid), transparent 70%),
      radial-gradient(ellipse 20% 28% at 98% 38%, var(--wash-light), transparent 70%),
      radial-gradient(ellipse 60% 22% at 50% 92%, var(--wash-deep), transparent 75%),
      radial-gradient(ellipse 40% 18% at 12% 82%, var(--wash-light), transparent 70%),
      radial-gradient(ellipse 36% 18% at 90% 80%, var(--wash-mid), transparent 70%);
  }
  .pouch__hole {
    position: absolute; left: 251px; top: 66px;
    width: 26px; height: 26px; border-radius: 50%;
    background: var(--backdrop); border: 2px solid var(--ink);
  }
  .brand {
    position: absolute; left: 0; right: 0; top: 150px;
  }
  .brand__name {
    font-size: 124px; line-height: 1; letter-spacing: 2px;
  }
  .brand__tagline {
    margin-top: 34px;
    font-family: "Poppins", Arial, sans-serif; font-weight: 500;
    font-size: 12px; letter-spacing: 7px;
  }
  .pack-info {
    position: absolute; left: 0; right: 0; top: 356px;
    font-size: 34px; line-height: 1;
  }
  .flavour {
    position: absolute; left: 0; right: 0; top: 420px;
    font-size: 80px; line-height: 1; color: var(--gold);
  }
  .product {
    position: absolute; left: 0; right: 0; top: 488px;
    font-size: 78px; line-height: 1;
  }
  .divider {
    position: absolute; left: 240px; top: 560px;
    width: 50px; height: 2px; background: var(--ink);
  }
  .subtitle {
    position: absolute; left: 0; right: 0; top: 574px;
    font-size: 46px; line-height: 1;
  }
  .claims {
    position: absolute; left: 146px; top: 622px;
    width: 250px; height: 124px;
    border: 2px solid var(--ink); border-radius: 12px;
    display: grid; grid-template-columns: 1fr 1fr;
    padding: 12px 12px; row-gap: 10px; column-gap: 6px;
    font-family: "Poppins", Arial, sans-serif; font-weight: 500;
    font-size: 9.5px; line-height: 1.25; text-align: left;
  }
  .claim { display: flex; align-items: center; gap: 8px; }
  .claim__icon { width: 32px; height: 32px; flex: none; }
  .weight {
    position: absolute; left: 386px; top: 810px;
    font-size: 36px; line-height: 1;
  }
</style>
</head>
<body>
  <main class="pouch">
    <div class="pouch__wash" role="img" aria-label="Soft yellow butterscotch watercolour wash"></div>
    <div class="pouch__hole"></div>

    <header class="brand">
      <div class="brand__name">Tarbery’s</div>
      <div class="brand__tagline">Irish Shortbread</div>
    </header>

    <p class="pack-info">12 Cookies | Bite Size</p>
    <h1 class="flavour">Butterscotch</h1>
    <p class="product">Shortbread</p>
    <div class="divider"></div>
    <p class="subtitle">Butterscotch Sables</p>

    <section class="claims">
      <div class="claim">
        <svg class="claim__icon" viewBox="0 0 32 32"><circle cx="16" cy="16" r="16" fill="#3a3a3a"/><path d="M9 16l5 5 9-10" fill="none" stroke="#fff" stroke-width="2.4" stroke-linecap="round" stroke-linejoin="round"/></svg>
        <span>No<br>Additives</span>
      </div>
      <div class="claim">
        <svg class="claim__icon" viewBox="0 0 32 32"><circle cx="16" cy="16" r="16" fill="#3a3a3a"/><path d="M21 8l3 3-9 9-3-3z" fill="none" stroke="#fff" stroke-width="1.8" stroke-linejoin="round"/><path d="M12 20l-3 4" stroke="#fff" stroke-width="1.8" stroke-linecap="round"/></svg>
        <span>No added<br>Colours</span>
      </div>
      <div class="claim">
        <svg class="claim__icon" viewBox="0 0 32 32"><circle cx="16" cy="16" r="16" fill="#3a3a3a"/><path d="M13 8h6M14 8v6l-5 9h14l-5-9V8" fill="none" stroke="#fff" stroke-width="1.8" stroke-linejoin="round"/></svg>
        <span>No Added<br>Preservatives</span>
      </div>
      <div class="claim">
        <svg class="claim__icon" viewBox="0 0 32 32"><circle cx="16" cy="16" r="16" fill="#3a3a3a"/><path d="M8 19l8-5 8 3-8 5z M8 19v3l8 3 8-5v-3" fill="none" stroke="#fff" stroke-width="1.6" stroke-linejoin="round"/></svg>
        <span>All Butter</span>
      </div>
    </section>

    <p class="weight">144gm</p>
  </main>
</body>
</html>
```